Brookhollow dog Kennel -Loyalty Card

We are a bod boarding and training Kennel located in Egypt and we would like to design a member loyalty card. The card need to be fun, funky. I would like the logo to appear on the card. On the back side we will list the benefits and on the bottom side of the card will will have the logos of our partner companies

Target Market(s)

clientele from dog lovers. Age 25 and above. 65% women.

Industry/Entity Type

Training

Font styles to use
Sans Serif

Colors
0555a3
33a6d7
0792cd

Requirements
Must have
• Brookhollow Logo and bleu colours.
Nice to have
• a dog figure
Should not have
• dark serious colours or aggressive looking dogs or dog breeds

```html
<!DOCTYPE html>
<html lang="en">
<head>
<meta charset="utf-8">
<title>Brookhollow dog Kennel – Loyalty Card</title>
<link href="https://fonts.googleapis.com/css2?family=Didact+Gothic&display=swap" rel="stylesheet">
<style>
  :root {
    --navy: #0555a3;
    --sky: #0792cd;
    --light-sky: #33a6d7;
    --deep: #0a4f9a;
    --yellow: #fff200;
    --plaid-red: #d8343c;
    --purple: #642a8c;
    --divider: #000000;
    --white: #ffffff;
    --logo-orange: #f7941d;
  }
  * { box-sizing: border-box; margin: 0; padding: 0; }
  html, body { width: 1034px; height: 1200px; overflow: hidden; background: var(--white); }
  body { font-family: "Didact Gothic", "Century Gothic", sans-serif; color: var(--yellow); }
  .canvas { position: relative; width: 1034px; height: 1200px; overflow: hidden; }

  .card { position: absolute; left: 0; width: 1034px; overflow: hidden; }
  .card--front { top: 0; height: 591px; background: var(--sky); }
  .card--back { top: 608px; height: 592px; background: var(--navy); }
  .divider { position: absolute; left: 0; top: 591px; width: 1034px; height: 17px; background: var(--divider); }

  .front-column { position: absolute; top: 0; left: 0; width: 162px; height: 100%; background: var(--navy); }
  .front-stripe { position: absolute; top: 0; left: 162px; width: 63px; height: 100%; background: var(--light-sky); }
  .back-stripe { position: absolute; top: 0; left: 0; width: 222px; height: 100%; background: var(--light-sky); }

  .dog-figure { position: absolute; border: 5px solid var(--yellow); }
  .dog-figure--plaid { left: 10px; top: 20px; width: 290px; height: 425px; border-radius: 40px 80px 30px 60px; background: var(--plaid-red); }
  .dog-figure--purple { left: -10px; top: 8px; width: 165px; height: 470px; border-radius: 0 90px 40px 0; background: var(--purple); }

  .headline { position: absolute; left: 300px; width: 640px; text-align: center; line-height: 1; font-weight: 400; }
  .headline__line { position: absolute; left: 0; width: 100%; font-size: 78px; }
  .headline__line--1 { top: 38px; }
  .headline__line--2 { top: 146px; }
  .turn-over { position: absolute; left: 365px; top: 236px; font-size: 48px; }

  .contact { position: absolute; left: 15px; width: 1034px; text-align: center; font-size: 34px; line-height: 1; }
  .contact--phone { top: 378px; left: -10px; }
  .contact--email { top: 428px; left: 15px; }
  .contact--web { top: 476px; left: 30px; }
  .contact--address { top: 524px; left: 10px; }
  .contact svg { vertical-align: -4px; margin-right: 8px; }

  .brand-mark { position: absolute; display: flex; align-items: center; gap: 10px; color: var(--yellow); line-height: 1.15; }
  .brand-mark__dot { background: var(--logo-orange); border-radius: 50%; flex: none; }
  .brand-mark--front { left: 760px; top: 290px; width: 260px; font-size: 34px; }
  .brand-mark--front .brand-mark__dot { width: 44px; height: 44px; }
  .brand-mark--back { left: 20px; top: 490px; font-size: 22px; }
  .brand-mark--back .brand-mark__dot { width: 28px; height: 28px; }

  .benefits { position: absolute; left: 241px; top: 158px; list-style: none; font-size: 36px; line-height: 49.5px; white-space: nowrap; }
  .benefit-markers { position: absolute; left: 168px; top: 176px; }
  .benefit-markers span { display: block; width: 50px; height: 14px; margin-bottom: 35.5px; border-radius: 7px; background: var(--deep); opacity: .7; }

  .partner-badge { position: absolute; top: 385px; width: 256px; height: 158px; background: var(--white); }
  .partner-badge--first { left: 340px; }
  .partner-badge--second { left: 637px; }
</style>
</head>
<body>
<main class="canvas">
  <section class="card card--front">
    <div class="front-column"></div>
    <div class="front-stripe"></div>
    <div class="dog-figure dog-figure--plaid" role="img" aria-label="Playful dog figure in a red tartan pattern with a yellow outline"></div>

    <h1 class="headline">
      <span class="headline__line headline__line--1">Loyalty has its</span>
      <span class="headline__line headline__line--2">benifits...</span>
    </h1>
    <p class="turn-over">(turn me over)</p>

    <div class="brand-mark brand-mark--front"><span class="brand-mark__dot"></span>Brookhollow Training</div>

    <p class="contact contact--phone"><svg width="44" height="30" viewBox="0 0 44 30" aria-hidden="true"><path fill="#fff200" d="M4 8c0-4 8-7 18-7s18 3 18 7v3h-9V7c-3-1-6-1-9-1s-6 0-9 1v4H4z"/><path fill="#fff200" d="M9 14h26l5 15H4z"/><circle cx="22" cy="21" r="4" fill="#0792cd"/></svg>(+20) 10 555 0123 4</p>
    <p class="contact contact--email"><svg width="38" height="28" viewBox="0 0 38 28" aria-hidden="true"><rect x="1.5" y="1.5" width="35" height="25" fill="none" stroke="#fff200" stroke-width="2.5"/><path d="M1.5 1.5 19 16 36.5 1.5M1.5 26.5 14 12M36.5 26.5 24 12" fill="none" stroke="#fff200" stroke-width="2.5"/></svg>info@bhdk.com</p>
    <p class="contact contact--web">www.brookhollowkennels.com</p>
    <p class="contact contact--address">14 Palm Grove Road, Giza Governorate, Egypt</p>
  </section>

  <div class="divider"></div>

  <section class="card card--back">
    <div class="back-stripe"></div>
    <div class="dog-figure dog-figure--purple" role="img" aria-label="Friendly purple dog figure with a yellow outline"></div>
    <div class="benefit-markers" aria-hidden="true"><span></span><span></span><span></span><span></span></div>
    <ul class="benefits">
      <li>5% discount on all 1 PawMart purchased</li>
      <li>10% discount on Suds &amp; Strolls services</li>
      <li>10% Discount on Brookhollow training courses</li>
      <li>One free trial for Day Care service</li>
    </ul>
    <div class="brand-mark brand-mark--back"><span class="brand-mark__dot"></span>Brookhollow</div>
    <div class="partner-badge partner-badge--first" role="img" aria-label="Partner badge"></div>
    <div class="partner-badge partner-badge--second" role="img" aria-label="Partner badge"></div>
  </section>
</main>
</body>
</html>
```